KRT business cards

I need a Business card design for my self. I am behavior analyst owner of a new company based in Miami. We offer Applied Behavior Analysis (ABA) services to individuals with developmental disabilities.

Business

```html
<!DOCTYPE html>
<html lang="en">
<head>
<meta charset="utf-8">
<title>KRT Business Cards</title>
<link href="https://fonts.googleapis.com/css2?family=Open+Sans:wght@400;600;700&family=Arimo:wght@400;700&display=swap" rel="stylesheet">
<style>
  :root {
    --backdrop: #1c1c1c;
    --green-light: #63c13f;
    --green-main: #22b14c;
    --green-deep: #1a8a3a;
    --green-title: #157a33;
    --leaf-pale: #d9ebc4;
    --navy: #1f2a8c;
    --ink: #2a2a2a;
    --paper: #ffffff;
    --paper-edge: #e6e6e6;
  }
  * { margin: 0; padding: 0; box-sizing: border-box; }
  html, body { width: 1000px; height: 1200px; overflow: hidden; }
  body { background: var(--backdrop); position: relative; font-family: "Open Sans", Arial, sans-serif; }

  .card {
    position: absolute;
    width: 600px;
    height: 343px;
    border-radius: 2px;
    overflow: hidden;
    box-shadow: 0 12px 30px rgba(0,0,0,.55);
  }

  /* Front */
  .card--front {
    left: 90px; top: 250px;
    background: linear-gradient(120deg, var(--green-light) 0%, var(--green-main) 55%, var(--green-main) 100%);
  }
  .front__emblem {
    position: absolute; left: 80px; top: 70px;
    width: 210px; height: 210px; border-radius: 50%;
    background: var(--green-deep); opacity: .55;
  }
  .front__identity {
    position: absolute; right: 36px; top: 188px; text-align: left;
  }
  .front__name { color: var(--paper); font-weight: 700; font-size: 17px; }
  .front__title { color: var(--green-title); font-size: 14px; line-height: 1.3; }

  /* Back */
  .card--back {
    left: 320px; top: 640px;
    background: linear-gradient(160deg, var(--paper) 0%, var(--paper-edge) 100%);
  }
  .back__decor {
    position: absolute; right: -60px; top: 10px;
    width: 300px; height: 300px; border-radius: 50%;
    background: radial-gradient(circle, var(--leaf-pale) 0%, rgba(217,235,196,.35) 60%, rgba(217,235,196,0) 72%);
  }
  .back__services { position: absolute; left: 330px; top: 34px; font-family: "Arimo", Arial, sans-serif; }
  .services__heading {
    color: var(--navy); font-weight: 700; font-size: 15px;
    padding-bottom: 4px; border-bottom: 2px solid var(--green-main); width: 210px;
  }
  .services__list { list-style: none; margin-top: 8px; }
  .services__item { font-size: 13px; color: var(--ink); display: flex; align-items: center; gap: 8px; margin-bottom: 5px; margin-left: 12px; }
  .services__item::before {
    content: ""; width: 8px; height: 8px; border-radius: 50%;
    border: 2.5px solid var(--navy); border-right-color: transparent;
  }
  .back__brand {
    position: absolute; left: 60px; top: 110px;
    display: flex; align-items: center; gap: 10px;
  }
  .brand__dot { width: 22px; height: 22px; border-radius: 50%; background: var(--green-main); }
  .brand__name { font-family: "Arimo", Arial, sans-serif; font-weight: 700; font-size: 34px; color: var(--navy); letter-spacing: 2px; }
  .back__contact { position: absolute; left: 60px; bottom: 40px; font-family: "Arimo", Arial, sans-serif; font-size: 17px; color: var(--ink); }
  .contact__row { display: flex; align-items: center; gap: 14px; margin-top: 8px; }
  .contact__icon { width: 16px; height: 16px; fill: var(--navy); }
</style>
</head>
<body>
  <section class="card card--front">
    <div class="front__emblem" role="img" aria-label="Company emblem area"></div>
    <div class="front__identity">
      <p class="front__name">Marisol Vega, B.A.</p>
      <p class="front__title">Board Certified Asst.<br>Behavior Analyst (BCABA)</p>
    </div>
  </section>

  <section class="card card--back">
    <div class="back__decor" role="img" aria-label="Faint emblem decoration"></div>
    <div class="back__services">
      <p class="services__heading">Applied Behavior Analysis :</p>
      <ul class="services__list">
        <li class="services__item">Parent/Teacher Training</li>
        <li class="services__item">Social Skills Training</li>
        <li class="services__item">Tutoring</li>
      </ul>
    </div>
    <div class="back__brand">
      <span class="brand__dot"></span>
      <span class="brand__name">KRT</span>
    </div>
    <div class="back__contact">
      <div class="contact__row">
        <svg class="contact__icon" viewBox="0 0 24 24" aria-hidden="true"><path d="M6.6 10.8a15 15 0 0 0 6.6 6.6l2.2-2.2a1 1 0 0 1 1-.25 11.4 11.4 0 0 0 3.6.57 1 1 0 0 1 1 1V20a1 1 0 0 1-1 1A17 17 0 0 1 3 4a1 1 0 0 1 1-1h3.5a1 1 0 0 1 1 1c0 1.25.2 2.45.57 3.57a1 1 0 0 1-.25 1z"/></svg>
        <span>305-555-0142</span>
      </div>
      <div class="contact__row">
        <svg class="contact__icon" viewBox="0 0 24 24" aria-hidden="true"><path d="M2 5h20v14H2z M2 5l10 8 10-8" /></svg>
        <span>m.vega.aba@mailnest.com</span>
      </div>
    </div>
  </section>
</body>
</html>
```